Home inspection business! professional look attracting customers just by looks. Read must haves

its a new business I started on my own for home inspections I would like something very professional to give to real estate agents and clients, its going to have my license number on it my business phone number my name my website as well etc on the back side it will be servicing areas and also what kind of services I offer I also have a business card from someone else the way I would like mine to be. I will attach my logo

Home Inspection

listed in nice to haves

• phone number - 555 293 8471
• website- hollowpinecheck.com
• license number #2938475610
• my name Gavin keropulis
• picture of my logo and me on the front
• on the back of the card. stating I am servicing All of New York and Long Island
• also services I will offer will be home inspection -mold inspection -lead inspection -radon inspection -Termite Inspection -Infared Scan.
• and also we provide inspections for single family homes condos co-ops town-homes
• and commercial property
• same colors as the logos and also if you recommend fonts to look like the logo not sure up to you

```html
<!DOCTYPE html>
<html lang="en">
<head>
<meta charset="utf-8">
<title>Hollow Pine Check Home Inspectors – Business Card</title>
<link href="https://fonts.googleapis.com/css2?family=Roboto:wght@400;500;700&family=Saira+Semi+Condensed:wght@600&display=swap" rel="stylesheet">
<style>
  :root {
    --page-bg: #c9c9c9;
    --brand-blue: #0f94d2;
    --brand-blue-deep: #0a86c4;
    --card-white: #f1f1f1;
    --ink-white: #ffffff;
    --ink-grey: #5a5a5a;
    --pill-bg: #e6e6e6;
    --rule: rgba(255,255,255,0.75);
  }
  * { box-sizing: border-box; margin: 0; padding: 0; }
  html, body { width: 1200px; height: 576px; overflow: hidden; }
  body {
    background: var(--page-bg);
    font-family: "Roboto", Arial, sans-serif;
    position: relative;
  }
  .card {
    position: absolute;
    top: 138px;
    width: 484px;
    height: 294px;
    border-radius: 10px;
    overflow: hidden;
    box-shadow: 0 3px 6px rgba(0,0,0,0.28);
  }
  /* ---------- services side ---------- */
  .card-services {
    left: 82px;
    background: linear-gradient(180deg, var(--brand-blue) 0%, var(--brand-blue-deep) 100%);
    color: var(--ink-white);
  }
  .card-services .backdrop-ring {
    position: absolute;
    left: 30px; top: 20px;
    width: 230px; height: 230px;
    border-radius: 50%;
    border: 26px solid rgba(0,60,110,0.12);
  }
  .brand-lockup {
    position: absolute;
    left: 0; right: 0; top: 62px;
    display: flex;
    align-items: center;
    justify-content: center;
    gap: 14px;
  }
  .brand-dot {
    width: 64px; height: 64px;
    border-radius: 50%;
    border: 7px solid var(--ink-white);
  }
  .brand-name {
    font-weight: 500;
    color: var(--ink-white);
    text-transform: uppercase;
    line-height: 1.05;
  }
  .brand-name .line-main { display: block; font-size: 27px; letter-spacing: 0.5px; }
  .brand-name .line-sub { display: block; font-size: 15px; letter-spacing: 5.4px; margin-top: 4px; }
  .services-heading {
    position: absolute;
    left: 34px; right: 34px; top: 197px;
    display: flex; align-items: center; gap: 10px;
  }
  .services-heading .rule { flex: 1; height: 1px; background: var(--rule); }
  .services-heading .pill {
    background: var(--pill-bg);
    color: var(--ink-grey);
    font-weight: 500;
    font-size: 12.5px;
    padding: 3px 12px;
    border-radius: 11px;
  }
  .services-list {
    position: absolute;
    left: 0; right: 0; top: 226px;
    text-align: center;
    font-size: 12.3px;
    line-height: 16px;
  }
  /* ---------- contact side ---------- */
  .card-contact { left: 602px; background: var(--brand-blue); }
  .card-contact .panel { position: absolute; inset: 0; }
  .holder {
    position: absolute; left: 23px; top: 25px; color: var(--ink-white);
  }
  .holder-name {
    font-family: "Saira Semi Condensed", "Arial Narrow", sans-serif;
    font-weight: 600; font-size: 19px; line-height: 22px;
  }
  .holder-title { font-size: 12.5px; margin-top: 3px; }
  .contact-list {
    position: absolute; left: 23px; top: 188px;
    list-style: none; color: var(--ink-white); font-size: 12.6px;
  }
  .contact-list li { display: flex; align-items: center; height: 18.3px; }
  .contact-list svg { width: 10px; height: 10px; margin-right: 10px; fill: var(--ink-white); }
  .vertical-brand {
    position: absolute;
    left: 412px; top: 147px;
    transform: translate(-50%, -50%) rotate(90deg);
    display: flex; align-items: center; gap: 12px;
    white-space: nowrap;
  }
  .vertical-brand .brand-dot { width: 44px; height: 44px; border-width: 5px; border-color: var(--ink-grey); }
  .vertical-brand .brand-name { color: var(--ink-grey); }
  .vertical-brand .line-main { font-size: 21px; }
  .vertical-brand .line-sub { font-size: 12px; letter-spacing: 4.2px; }
</style>
</head>
<body>

<section class="card card-services" aria-label="Services side">
  <div class="backdrop-ring"></div>
  <div class="brand-lockup">
    <div class="brand-dot"></div>
    <div class="brand-name">
      <span class="line-main">Hollow Pine Check</span>
      <span class="line-sub">Home Inspectors</span>
    </div>
  </div>
  <div class="services-heading">
    <span class="rule"></span><span class="pill">OUR SERVICES</span><span class="rule"></span>
  </div>
  <p class="services-list">
    Home Inspection&nbsp; | &nbsp;Mold Inspection&nbsp; | &nbsp;Lead Inspection&nbsp; | &nbsp;Radon Inspection<br>
    Termite Inspection&nbsp; | &nbsp;Infared Scan&nbsp; | &nbsp;Single Family Homes<br>
    Condos Co-ops Town&nbsp; | &nbsp;&nbsp;Homes &amp; Commercial Property
  </p>
</section>

<section class="card card-contact" aria-label="Contact side">
  <svg class="panel" viewBox="0 0 481 294" preserveAspectRatio="none" aria-hidden="true">
    <path d="M312 0 Q262 150 306 294 L481 294 L481 0 Z" fill="var(--card-white)"/>
    <path d="M312 0 Q262 150 306 294 L298 294 Q252 150 304 0 Z" fill="#6b6b6b"/>
  </svg>
  <div class="holder">
    <div class="holder-name">Gavin Keropulis</div>
    <div class="holder-title">Managing Director</div>
  </div>
  <ul class="contact-list">
    <li><svg viewBox="0 0 10 10"><path d="M1 3 Q5 0 9 3 L8 4.5 L6.5 3.8 L6.5 3 Q5 2.4 3.5 3 L3.5 3.8 L2 4.5 Z M2.5 5 L7.5 5 L8.5 9 L1.5 9 Z"/></svg>555 293 8471</li>
    <li><svg viewBox="0 0 10 10"><path d="M0.5 2 L9.5 2 L5 5.5 Z M0.5 3 L5 6.5 L9.5 3 L9.5 8.5 L0.5 8.5 Z"/></svg>gavin@hollowpinecheck.com</li>
    <li><svg viewBox="0 0 10 10"><circle cx="5" cy="5" r="4.2" fill="none" stroke="#fff" stroke-width="1"/><ellipse cx="5" cy="5" rx="1.8" ry="4.2" fill="none" stroke="#fff" stroke-width="0.9"/><path d="M1 5 H9" stroke="#fff" stroke-width="0.9"/></svg>www.hollowpinecheck.com</li>
    <li><svg viewBox="0 0 10 10"><path d="M3 1 L2 9 M7 1 L6 9 M0.8 3.5 H9.5 M0.5 6.5 H9.2" stroke="#fff" stroke-width="1.3" fill="none"/></svg>License No.: #2938475610</li>
  </ul>
  <div class="vertical-brand">
    <div class="brand-dot"></div>
    <div class="brand-name">
      <span class="line-main">Hollow Pine Check</span>
      <span class="line-sub">Home Inspectors</span>
    </div>
  </div>
</section>

</body>
</html>
```